Website Design for PawRank - New Digital Agency

We are creating a new digital marketing agency and need a new website. I have attached the logo. Our niche is going to be veterinarians. Use the same colors as in the logo (blue, white and gray).

I want real pictures of real people in this and not just boring stock photos. It needs to be related to the industry.

Home page (example:https://linkvorta.com/)
Service page (example: https://darvimosk.com/consulting/)
Case study page (example: https://www.tomaswellbry.com/seo/case-study/)

I will continue to update this brief.
Updates

I updated the brief with some additional sample sites 2 days ago and want to see more designs. I won't need that may more days ...just a few more.

Target Market(s)

veterinarians

Font styles to use
Sans Serif

Requirements
Must have
• I want a very clean looking site. Use the same colors as in the logo (blue, white and gray).
Nice to have
• We need to build this with the idea that the purpose is to generate leads for our business.
• Home page (example:https://linkvorta.com/)
• Service page (example: https://darvimosk.com/consulting/)
• Case study page (example: https://www.tomaswellbry.com/seo/case-study/)

```html
<!DOCTYPE html>
<html lang="en">
<head>
<meta charset="utf-8">
<title>PawRank – More Traffic for Veterinarians</title>
<link rel="stylesheet" href="https://fonts.googleapis.com/css2?family=Montserrat:wght@400;500;600;700&family=Playfair+Display:ital@1&display=swap">
<style>
:root{
  --blue:#0f56a3;
  --blue-soft:#2b6bb2;
  --orange:#f8a51d;
  --ink:#333;
  --gray:#5e5e5e;
  --gray-light:#f1f1f1;
  --white:#fff;
}
*{box-sizing:border-box;margin:0;padding:0}
html,body{width:1200px;height:4084px;overflow:hidden}
body{position:relative;font-family:'Montserrat',sans-serif;color:var(--ink);background:var(--white)}
.abs{position:absolute}
.accent{color:var(--blue)}
.btn{position:absolute;display:flex;align-items:center;justify-content:center;background:var(--orange);color:#222;font-weight:600;border-radius:40px;box-shadow:0 10px 22px rgba(248,165,29,.35);text-decoration:none}
.media{position:absolute}

/* hero */
.hero{position:absolute;left:0;top:0;width:1200px;height:594px;background:linear-gradient(180deg,#f4f4f4 0%,#fafafa 70%,#fff 100%)}
.hero-photo{left:548px;top:80px;width:652px;height:514px;background:linear-gradient(120deg,#eef0f2 0%,#d9e0e8 45%,#8aa9c9 70%,#e4e6e8 100%)}
.logo{left:76px;top:32px;font-size:30px;font-weight:700;color:var(--blue)}
.nav{left:648px;top:40px;display:flex;gap:24px;font-size:13px;color:#333}
.nav-cta{left:984px;top:27px;width:145px;height:41px;font-size:13px}
.hero-title{left:80px;top:146px;font-size:48px;font-weight:700;line-height:56px;color:#333}
.hero-sub{left:80px;top:334px;width:430px;font-size:14px;line-height:24px;color:#444}
.field{position:absolute;background:var(--gray-light);border-radius:40px;display:flex;align-items:center;padding-left:32px;font-size:13px;color:#555}
.hero-field{left:68px;top:409px;width:439px;height:60px}
.hero-btn{left:362px;top:417px;width:145px;height:47px;font-size:13px}

/* press */
.press{left:150px;top:626px;width:900px;display:flex;justify-content:space-between;align-items:center;color:#a4a4a4;font-size:28px;font-weight:600}

/* testimonial */
.band{left:0;top:758px;width:1200px;height:428px;background:var(--blue)}
.qmark{font-family:'Montserrat',sans-serif;font-weight:700;font-size:220px;line-height:1;color:var(--blue-soft)}
.quote{left:300px;top:866px;width:600px;text-align:center;color:var(--white);font-size:27px;line-height:38px}
.quote-by{left:0;top:1038px;width:1200px;text-align:center;color:var(--white);font-size:14px;font-weight:500}
.avatar{position:absolute;border-radius:50%;border:3px solid var(--white);background:radial-gradient(circle at 50% 45%,#bfbfbf,#6d6d6d)}
.avatar.active{background:radial-gradient(circle at 50% 45%,#7e8fa6,#10284a);border-color:var(--blue)}

/* story */
.card{left:124px;top:1360px;width:313px;height:455px;background:var(--white);box-shadow:0 8px 30px rgba(0,0,0,.1)}
.card-text{left:158px;top:1400px;width:255px;font-family:'Playfair Display',serif;font-style:italic;font-size:24px;line-height:36px;color:#888}
.pets{left:171px;top:1720px;width:284px;height:142px;background:linear-gradient(90deg,#c99f70,#8e8e8e,#6f5640,#3b3b3b,#c08a55);border-radius:40px 40px 8px 8px}
.story-title{left:540px;top:1352px;width:560px;font-size:41px;font-weight:700;line-height:51px;color:#333}
.body{position:absolute;left:540px;width:530px;font-size:14px;letter-spacing:.25px;line-height:29px;color:#333}
.photo-vet{left:540px;top:1742px;width:533px;height:312px;background:linear-gradient(120deg,#e9ecee,#f5f2ef 40%,#c9a48a 55%,#f2f2f2 75%,#dadedf)}
.photo-exam{left:540px;top:2441px;width:533px;height:330px;background:linear-gradient(120deg,#f1f1f1,#cfd9e4 40%,#6a8fb8 55%,#9aa0a6 70%,#eeeeee)}
.read-btn{left:528px;top:2975px;width:345px;height:54px;font-size:14px}

.rule{position:absolute;left:124px;width:69px;height:2px;background:var(--blue)}
.side-title{left:124px;top:1988px;width:320px;font-size:26px;font-weight:700;line-height:37px;color:#333}
.side-text{left:124px;top:2072px;width:300px;font-size:14px;letter-spacing:.2px;line-height:27px;color:#333}
.side-btn{left:119px;top:2343px;width:234px;height:44px;font-size:13px}

/* cta + footer */
.foot{left:0;top:3173px;width:1200px;height:911px;background:var(--blue)}
.cta-photo{left:0;top:3173px;width:600px;height:600px;background:linear-gradient(135deg,#e9e9e9 0%,#c3cfdc 50%,#4d76a6 100%)}
.cta-title{left:661px;top:3340px;width:480px;font-size:40px;font-weight:700;line-height:52px;color:var(--white)}
.cta-sub{left:666px;top:3514px;width:460px;font-size:14px;line-height:24px;color:#dfe9f5}
.cta-field{left:648px;top:3598px;width:374px;height:60px;background:var(--white)}
.cta-btn{left:946px;top:3605px;width:148px;height:47px;font-size:13px}
.cols{left:634px;top:3816px;display:flex;gap:0}
.col{width:140px;color:#cfdcee;font-size:12px;line-height:25px}
.col:nth-child(1){width:141px}.col:nth-child(2){width:121px}.col:nth-child(3){width:103px}
.col h4{font-size:13.5px;font-weight:700;color:#cfdcee;margin-bottom:12px}
.social{left:1024px;top:4010px;display:flex;gap:15px}
.social span{width:14px;height:14px;border-radius:50%;background:#cfdcee}
</style>
</head>
<body>

<section class="hero" aria-label="Hero">
  <div class="media hero-photo" role="img" aria-label="Veterinarian in blue scrubs smiling at a seated grey merle dog in a clinic"></div>
  <div class="abs logo">PawRank</div>
  <nav class="abs nav"><span>Home</span><span>About</span><span>Tools</span><span>Newsletter</span><span>Contact</span></nav>
  <a class="btn nav-cta">Sign up/Login</a>
  <h1 class="abs hero-title">Get <span class="accent">More Traffic</span> to<br>your Veterinarian<br>Website</h1>
  <p class="abs hero-sub">Enter your email below to get access to my proven SEO and traffic tips</p>
  <div class="field hero-field">Email Address</div>
  <a class="btn hero-btn">Sign Up Now!</a>
</section>

<div class="abs press" aria-label="As featured in">
  <span>Brightwell</span><span>Dailyfold</span><span>Norvane</span><span>Kestrel Market</span><span>Brightwell</span>
</div>

<section aria-label="Testimonial">
  <div class="abs band"></div>
  <div class="abs qmark" style="left:108px;top:830px">“</div>
  <div class="abs qmark" style="left:978px;top:965px">”</div>
  <blockquote class="abs quote">Lorem ipsum dolor sit amet, ea pro brute facer propriae, nec epicurei senserit pericula cu. Ea graece animal equidem cum. Ei graece omittantur vel scaevola qui te.</blockquote>
  <p class="abs quote-by">Daniel Morrow - Author &amp; Marketer</p>
  <div class="avatar" role="img" aria-label="Client portrait" style="left:263px;top:1138px;width:96px;height:96px"></div>
  <div class="avatar" role="img" aria-label="Client portrait" style="left:401px;top:1138px;width:96px;height:96px"></div>
  <div class="avatar active" role="img" aria-label="Portrait of the quoted author" style="left:527px;top:1114px;width:144px;height:144px"></div>
  <div class="avatar" role="img" aria-label="Client portrait" style="left:702px;top:1138px;width:96px;height:96px"></div>
  <div class="avatar" role="img" aria-label="Client portrait" style="left:840px;top:1138px;width:96px;height:96px"></div>
</section>

<section aria-label="Case story">
  <div class="abs card"></div>
  <p class="abs card-text">Lorem ipsum dolor sit amet, ea pro brute elit facer lorem propriae, nec epicurei senserit pericula cu. Ea graece animal equidem cum. Ei graece omittantur vel scaevola qui te.</p>
  <div class="media pets" role="img" aria-label="Group of dogs and cats sitting together"></div>

  <h2 class="abs story-title">See How I Got <span class="accent">More Web Traffic</span> to my Veterinary Website</h2>
  <p class="body" style="top:1530px">Lorem ipsum dolor sit amet, ea pro brute facer propriae, nec epicurei senserit pericula cu. Ea graece animal equidem cum. Ei graece omittantur vel. Habeo persius scaevola qui te. Duo eu mucius nostrum. Causae docendi temporibus vel at. Usu ad postea fabellas, qui nostro iracundia ei. Te vis dicat ludus, an per tale detraxit. Quis vulputate ea pri, essent noluisse sea ex, te nam enim falli. Inciderint temporibus ne cum</p>
  <div class="media photo-vet" role="img" aria-label="Smiling veterinarian in a white coat seated at a desk"></div>
  <p class="body" style="top:2104px">Id quo munere delenit accusamus, his id probatus eleifend, ei fugit simul sed. Cu maiorum suscipiantur sit. Te vis dicat ludus, an per tale detraxit. Quis vulputate ea pri, essent noluisse sea ex, te nam enim falli. Inciderint temporibus ne cum.</p>
  <p class="body" style="top:2248px">Lorem ipsum dolor sit amet, ea pro brute facer propriae, nec epicurei senserit pericula cu. Ea graece animal equidem cum. Ei graece omittantur vel. Habeo persius scaevola qui te. Duo eu mucius nostrum. Causae docendi temporibus vel at. Usu ad postea fabellas, qui nostro iracundia ei. Quo eirmod nostrum intellegebat ad, id duo accusamus.</p>
  <div class="media photo-exam" role="img" aria-label="Veterinarian examining a dog lying on a table with a stethoscope"></div>
  <p class="body" style="top:2824px">Prima cetero intellegebat id eum, ius iriure impetus no, enim nominati suscipiantur cu pro. Eum an aliquid adipisci praesent, id pro laoreet feugait incorrupte. Ex sed probo nihil quidam. Meliore docendi mandamus ius no. Quo eirmod nostrum intellegebat ad, id duo accusamus</p>
  <a class="btn read-btn">Read More about Getting Results</a>

  <div class="rule" style="top:1945px"></div>
  <h3 class="abs side-title">The best part? <span class="accent">It’s a simple, 3-step formula</span></h3>
  <p class="abs side-text">The formula takes hard work. But it’s not complicated. And it’s one of the fastest ways I’ve discovered to quickly grow your organic traffic.<br><br>If you want to get access to this strategy (including a real-life case study of The Staircase Method in action), just enter your email address below and I’ll send it over.</p>
  <a class="btn side-btn">View the case study</a>
  <div class="rule" style="top:2441px"></div>
</section>

<footer aria-label="Sign up and footer">
  <div class="abs foot"></div>
  <div class="media cta-photo" role="img" aria-label="Veterinarian with stethoscope checking a grey merle dog"></div>
  <h2 class="abs cta-title">Do You Want More Traffic to your Veterinary Website?</h2>
  <p class="abs cta-sub">Enter your email below to get access to my proven SEO and traffic tips</p>
  <div class="field cta-field">Email Address</div>
  <a class="btn cta-btn">Sign Up Now!</a>

  <div class="abs cols">
    <div class="col"><h4>What We Do</h4>Solutions<br>Products<br>Resources<br>Our Customers</div>
    <div class="col"><h4>Company</h4>About Us<br>Our Team<br>Careers<br>Legal<br>Contact</div>
    <div class="col"><h4>Support</h4>Features<br>Pricing<br>Team<br>Contact<br>Login</div>
    <div class="col"><h4>Legal</h4>Legal<br>Terms Of Service<br>Privacy Policy</div>
  </div>
  <div class="abs social" aria-label="Social links"><span></span><span></span><span></span></div>
</footer>

</body>
</html>
```